Kalm to Bloom: Prespective and Balence in People's Lives Needs a Buissness Card Design

Calm to Bloom Community Center is an organization that seeks to quiet steps toward a steadier day. Main services include: guided meditation, group brainstorming, and guided counseling. Calm to Bloom combines Eastern practices, i.e. Buddhism, Hinduism, and Taoism, with Western practices: therapy, group brainstorming and healing. We would like a double sided card: 1) front vertical with image, 2) back horizontal with information. The main colors for the card are red, white, black. Different finishes would be nice--please no high gloss. Matte, pearlized, embossing--used tactfully and sparingly would be nice. The card should convey balance/harmony in a modern world.

```html
<!DOCTYPE html>
<html lang="en">
<head>
<meta charset="utf-8">
<title>Calm to Bloom – Business Card</title>
<link href="https://fonts.googleapis.com/css2?family=Quicksand:wght@300;400;500&display=swap" rel="stylesheet">
<style>
  :root {
    --ink: #262626;
    --paper: #ecebe9;
    --red: #b23a2b;
    --white: #ffffff;
    --stage: #d9d7d4;
    --muted: #cfcfcf;
  }
  * { box-sizing: border-box; margin: 0; padding: 0; }
  html, body { width: 1200px; height: 872px; overflow: hidden; }
  body {
    background: var(--stage);
    font-family: "Quicksand", sans-serif;
    position: relative;
  }
  .card { position: absolute; overflow: hidden; box-shadow: 0 2px 6px rgba(0,0,0,.18); background: var(--paper); }

  /* Front – vertical */
  .card-front { left: 140px; top: 164px; width: 320px; height: 544px; }
  .front-dark { position: absolute; left: 160px; top: 0; width: 160px; height: 100%; background: var(--ink); }
  .front-brand {
    position: absolute; left: 0; top: 258px; width: 160px;
    display: flex; align-items: center; justify-content: center; gap: 8px;
  }
  .brand-dot { width: 16px; height: 16px; border-radius: 50%; background: var(--red); flex: none; }
  .brand-name { color: var(--ink); font-size: 17px; font-weight: 400; letter-spacing: .3px; white-space: nowrap; }

  /* Back – horizontal */
  .card-back { left: 530px; top: 276px; width: 560px; height: 320px; }
  .org-band {
    position: absolute; left: 236px; top: 14px; width: 310px; height: 50px;
    background: var(--ink); color: var(--white); padding: 6px 12px; text-align: right;
  }
  .org-name { font-size: 17px; font-weight: 400; letter-spacing: .3px; line-height: 1.2; white-space: nowrap; }
  .org-tagline { font-size: 9px; font-weight: 300; color: var(--muted); margin-top: 2px; }
  .info-block { position: absolute; left: 0; top: 74px; width: 484px; height: 246px; background: var(--ink); }
  .name-box {
    position: absolute; left: 210px; top: 86px; width: 262px; height: 86px;
    border: 2px solid var(--paper); padding: 6px 14px; color: var(--white);
  }
  .person-name { font-size: 40px; font-weight: 300; line-height: 1.1; white-space: nowrap; }
  .person-role { font-size: 17px; font-weight: 300; }
  .contacts { position: absolute; left: 22px; top: 196px; list-style: none; color: var(--white); font-size: 11px; font-weight: 300; }
  .contacts li { display: flex; align-items: center; gap: 8px; margin-bottom: 9px; }
  .contacts svg { width: 12px; height: 12px; flex: none; }
</style>
</head>
<body>
  <section class="card card-front" aria-label="Card front">
    <div class="front-dark"></div>
    <div class="front-brand">
      <span class="brand-dot"></span>
      <span class="brand-name">Calm to Bloom</span>
    </div>
  </section>

  <section class="card card-back" aria-label="Card back">
    <div class="org-band">
      <p class="org-name">Calm to Bloom Community Center</p>
      <p class="org-tagline">"quiet steps toward a steadier day"</p>
    </div>
    <div class="info-block"></div>
    <div class="name-box">
      <p class="person-name">Mara Ellison</p>
      <p class="person-role">Sales manager</p>
    </div>
    <ul class="contacts">
      <li>
        <svg viewBox="0 0 12 12"><circle cx="6" cy="6" r="5" fill="none" stroke="#fff"/><path d="M1 6h10M6 1c2 2 2 8 0 10M6 1c-2 2-2 8 0 10" fill="none" stroke="#fff" stroke-width=".8"/></svg>
        www.calmtobloom.org
      </li>
      <li>
        <svg viewBox="0 0 12 12"><path d="M6 11s-4-4-4-6.5a4 4 0 0 1 8 0C10 7 6 11 6 11z" fill="#fff"/><circle cx="6" cy="4.5" r="1.4" fill="#262626"/></svg>
        Lantern House 12, Road 7, Riverside
      </li>
      <li>
        <svg viewBox="0 0 12 12"><rect x="1" y="2.5" width="10" height="7" fill="none" stroke="#fff"/><path d="M1 2.5l5 4 5-4" fill="none" stroke="#fff"/></svg>
        hello@calmtobloom.org
      </li>
      <li>
        <svg viewBox="0 0 12 12"><rect x="3" y="1" width="6" height="10" rx="1" fill="none" stroke="#fff"/><circle cx="6" cy="9" r=".7" fill="#fff"/></svg>
        1240 555 0182
      </li>
    </ul>
  </section>
</body>
</html>
```